Business Card Upgrade

I have designed our business card using our new logo. I think it needs imporovements. We used to have two cards for our business. One card was for our software business, and the other was for our consulting business. We are now in the process of combining our websites, marketing, name, and a new logo.

Our goal is to have a really sharp professional logo. One reason I designed the card the way I did was that our Titles are sometimes long, and by separating the person's name and title, it shows up very well and the title can be adjusted no matter how long it is. Sometimes the title can be 4 or 5 words or more.

We really like our logo on black as it shows up very nice. Our PMS colors are as follows: 368C and 459C.

The Designer that will be working with us will need to deliver the following:

The front and back of the Business Card Design will need to be delivered in a high quality JPEG, and
The front and back of the Business Card Design in Illustrator Format .ai
Any fonts will need to be sent to us if they are not standard and are required to open the Illustrator file correctly.

To help us get a good idea of the card with a title, please use the title: " Director of Software Development "

NOTE: The chosen designer will be selected to design our new letterhead within 2 weeks from the closing of this contest.

To help us make sure the card design works with longer titles, please use the followign job title on the card:  

"Director of Software and Product Development"

 

ALL DESIGNERS:

1. I appreciate the different angles you are showing the cards, but please be sure and always show the direct view, so I can see the layout and what the person I hand the card will see.

2. Please do not use white.  Please use off white as I don't care for white cards and they get dirty easy and do not represent the designs well.

Dear Designers,

Please provide samples straight one as a viewer of the card will see.  Some of the angles that are presented make it impossible to tell how everything fits, and sometimes even makes areas look skewed. So, please provide a straight sample view.

Pinnacle 400 company executives such as Vice Presidents, and Directors

Software

• Professional looking Card.

Our customers are Directors, Vice Presidents, and Presidents of companies as large as Pinnacle 400 companies. The card needs to get attention wile still looking professional.

Delivery of the finished product in Illustrator Format with any fonts needed to edit the text or open the file.

The card will be a heavy stock with a soft touch coating for that silk feel.

```html
<!DOCTYPE html>
<html lang="en">
<head>
<meta charset="utf-8">
<title>Harborline Trade Group – Business Card</title>
<link rel="stylesheet" href="https://fonts.googleapis.com/css2?family=Lato:wght@400;700;900&display=swap">
<style>
  :root {
    --canvas-bg: #d9d4cc;
    --card-black: #0b0b0b;
    --card-glow: #262626;
    --brand-green: #5cb345;
    --brand-cream: #e6d79c;
    --shadow: rgba(0, 0, 0, 0.45);
  }
  * { margin: 0; padding: 0; box-sizing: border-box; }
  html, body { width: 1200px; height: 1000px; overflow: hidden; }
  body {
    background: var(--canvas-bg);
    font-family: "Lato", Arial, sans-serif;
    position: relative;
  }
  .card {
    position: absolute;
    background: radial-gradient(ellipse at 50% 30%, var(--card-glow) 0%, var(--card-black) 70%);
    box-shadow: 4px 6px 10px var(--shadow);
    overflow: hidden;
  }
  .card--front { left: 122px; top: 64px; width: 692px; height: 395px; }
  .card--back  { left: 420px; top: 521px; width: 693px; height: 394px; }

  .front__accent-bar {
    position: absolute; left: 0; top: 0; width: 11px; height: 100%;
    background: var(--brand-green);
  }
  .front__name {
    position: absolute; left: 360px; top: 82px;
    color: var(--brand-green); font-size: 25px; font-weight: 400; letter-spacing: 1px;
  }
  .front__title {
    position: absolute; left: 361px; top: 112px;
    color: var(--brand-cream); font-size: 16px; font-weight: 400;
  }
  .contact-list {
    position: absolute; left: 367px; top: 174px; list-style: none;
    color: var(--brand-cream); font-size: 15px;
  }
  .contact-list li { display: flex; align-items: flex-start; height: 24.5px; }
  .contact-list svg { width: 14px; height: 14px; margin: 2px 9px 0 0; flex: none; fill: var(--brand-green); }
  .contact-list .address { line-height: 19px; }

  .front__company-name {
    position: absolute; left: 48px; top: 268px;
    color: var(--brand-green); font-size: 36px; font-weight: 900;
    line-height: 40px; letter-spacing: 2px;
  }
  .services {
    position: absolute; left: 0; right: 0; top: 367px; text-align: center; padding-left: 12px;
    color: var(--brand-green); font-family: Arial, "Lato", sans-serif; font-size: 14px; letter-spacing: 0.3px;
  }
  .services .divider { color: var(--brand-cream); margin: 0 5px; }

  .back__tagline {
    position: absolute; left: 0; right: 0; top: 32px; text-align: center;
    color: var(--brand-cream); font-family: Arial, "Lato", sans-serif; font-size: 13.5px; letter-spacing: 1px;
  }
  .back__tagline .highlight { color: var(--brand-green); }
  .back__company-name {
    position: absolute; left: 0; right: 0; top: 140px; text-align: center;
    color: var(--brand-green); font-size: 62px; font-weight: 900;
    line-height: 70px; letter-spacing: 4px;
  }
  .back__website {
    position: absolute; left: 0; right: 0; top: 355px; text-align: center;
    color: var(--brand-cream); font-size: 17px; font-weight: 700;
  }
  .back__website .highlight { color: var(--brand-green); }
</style>
</head>
<body>

<section class="card card--front" aria-label="Business card front">
  <div class="front__accent-bar"></div>

  <h1 class="front__name">DANA WHITFIELD</h1>
  <p class="front__title">Director of Software Development</p>

  <ul class="contact-list">
    <li>
      <svg viewBox="0 0 16 16" aria-hidden="true"><path d="M1 6c0-3 4-4 7-4s7 1 7 4v1h-4V5.5H5V7H1zM3 8h10l1 6H2z"/></svg>
      <span>+ 555.010.2846</span>
    </li>
    <li>
      <svg viewBox="0 0 16 16" aria-hidden="true"><path d="M1 3h14v10H1z M2 4l6 5 6-5" stroke="#0b0b0b" stroke-width="1"/></svg>
      <span>dwhitfield@harborlinetrade.com</span>
    </li>
    <li>
      <svg viewBox="0 0 16 16" aria-hidden="true"><circle cx="8" cy="8" r="6.5" fill="none" stroke="var(--brand-green)" stroke-width="1.5"/><path d="M1.5 8h13M8 1.5c-3 3.5-3 9.5 0 13M8 1.5c3 3.5 3 9.5 0 13" fill="none" stroke="var(--brand-green)" stroke-width="1.2"/></svg>
      <span>harborlinetrade.com</span>
    </li>
    <li>
      <svg viewBox="0 0 16 16" aria-hidden="true"><path d="M8 0.5a5 5 0 0 1 5 5c0 4-5 10-5 10s-5-6-5-10a5 5 0 0 1 5-5z"/><circle cx="8" cy="5.5" r="2" fill="#0b0b0b"/></svg>
      <span class="address">480 Cedar Bend Lane<br>Fairport, AL 36000</span>
    </li>
  </ul>

  <p class="front__company-name">HARBORLINE<br>TRADE GROUP</p>

  <p class="services">CONSULTING<span class="divider">|</span>SOFTWARE<span class="divider">|</span>OPERATIONS<span class="divider">|</span>ADMINISTRATION</p>
</section>

<section class="card card--back" aria-label="Business card back">
  <p class="back__tagline">THE ONLY FRIM WITH ENOUGH EXPERTISE TO OFFER EVERY <span class="highlight">FTZ</span> SOLUTIONS</p>
  <p class="back__company-name">HARBORLINE<br>TRADE GROUP</p>
  <p class="back__website">WWW.<span class="highlight">HARBORLINETRADE</span>.COM</p>
</section>

</body>
</html>
```